Commercial printing and sign company printed advertisement.

We're wanting a new look for our printed advertisements. We've been in business for 40 years and have been pushing hard the last couple of years to grow our business. Our target market is changing and our client base is changing. I am looking for advertisement that appeals to larger companies. However, we are not stuffy people so I would like the ads to convey our professionalism but also stand out with color and have a fun side. I'm currently needing advertisements for a printed magazine, printed newspaper, web ads and a table top at a local restaurant. We have our traditional four color logo (swoosh) as well as a simpler single color option. I am attaching various ads we have done previously so you can see what we have. It is important for these ads to convey the different things we do - as we do alot!

```html
<!DOCTYPE html>
<html lang="en">
<head>
<meta charset="utf-8">
<title>Redline Printing – Advertisement</title>
<link rel="stylesheet" href="https://fonts.googleapis.com/css2?family=Montserrat:wght@700&display=swap">
<style>
  :root {
    --backdrop: #54585b;
    --paper: #ffffff;
    --ink: #1a1a1a;
    --brand-red: #e31b3b;
    --accent-yellow: #f0e81c;
    --accent-cyan: #1c9ad6;
    --footer: #000000;
  }
  html, body {
    margin: 0;
    padding: 0;
    width: 903px;
    height: 1200px;
    overflow: hidden;
    background: var(--backdrop);
  }
  .ad-frame {
    position: absolute;
    left: 21px;
    top: 293px;
    width: 861px;
    height: 613px;
    box-shadow: 4px 6px 10px rgba(0,0,0,0.45);
  }
  .ad {
    position: absolute;
    left: 0;
    top: 0;
    width: 1250px;
    height: 890px;
    transform: scale(0.6888);
    transform-origin: 0 0;
    background: var(--paper);
    overflow: hidden;
    font-family: "Montserrat", sans-serif;
    font-weight: 700;
  }
  .brand {
    position: absolute;
    top: 120px;
    left: 0;
    width: 100%;
    margin: 0;
    text-align: center;
    font-family: "Montserrat", sans-serif;
    font-weight: 700;
    font-size: 112px;
    line-height: 1;
    color: var(--brand-red);
    white-space: nowrap;
  }
  .brand__dot {
    display: inline-block;
    width: 44px;
    height: 44px;
    border-radius: 50%;
    background: var(--brand-red);
    margin-right: 22px;
    vertical-align: 10px;
  }
  .services {
    position: absolute;
    top: 396px;
    left: 0;
    width: 100%;
    margin: 0;
    padding: 0;
    list-style: none;
    text-align: center;
    font-size: 35px;
    line-height: 57px;
    color: var(--ink);
  }
  .services__row { white-space: nowrap; }
  .services__item { margin: 0 12px; }
  .services__item--dot::before {
    content: "";
    display: inline-block;
    width: 22px;
    height: 22px;
    border-radius: 50%;
    background: var(--brand-red);
    margin-right: 8px;
    vertical-align: 2px;
  }
  .footer-rule {
    position: absolute;
    left: 0;
    top: 716px;
    width: 100%;
    height: 10px;
    background: var(--accent-yellow);
  }
  .footer-band {
    position: absolute;
    left: 0;
    top: 726px;
    width: 100%;
    height: 164px;
    background: var(--footer);
  }
  .contact {
    position: absolute;
    right: 67px;
    top: 795px;
    text-align: right;
    font-style: normal;
    font-size: 28px;
    line-height: 37px;
  }
  .contact__web { color: var(--accent-yellow); }
  .contact__address { color: var(--accent-cyan); }
</style>
</head>
<body>
  <div class="ad-frame">
    <article class="ad">
      <h1 class="brand"><span class="brand__dot"></span>Redline Printing</h1>

      <ul class="services">
        <li class="services__row">
          <span class="services__item services__item--dot">PRINTING</span>
          <span class="services__item services__item--dot">SIGNS</span>
          <span class="services__item services__item--dot">BANNERS</span>
          <span class="services__item services__item--dot">POSTERS</span>
          <span class="services__item services__item--dot">DECALS</span>
        </li>
        <li class="services__row">
          <span class="services__item services__item--dot">DESIGN</span>
          <span class="services__item services__item--dot">SCREEN PRINTING</span>
          <span class="services__item services__item--dot">EMBROIDERY</span>
        </li>
        <li class="services__row">
          <span class="services__item">BLUE PRINTS</span>
          <span class="services__item services__item--dot">PROMOTIONAL ITEMS</span>
        </li>
        <li class="services__row">&amp; SO MUCH MORE!!</li>
      </ul>

      <div class="footer-rule"></div>
      <div class="footer-band"></div>

      <address class="contact">
        <div class="contact__web">WWW.REDLINEPRINTING.COM</div>
        <div class="contact__address">840 N. MAIN ST | MAPLE RIDGE, MO</div>
      </address>
    </article>
  </div>
</body>
</html>
```